Business Card Design

We are a project managment company specializing in Interior fitout
VRK is for Commercial, Domestic, Industial - we provide managment to these industries and see the projects through design to contruction
Would like an area on the back of the card where peoplr can write notes
Thinking laser lines and architectural finishes
Colour theme at the moment is light grey and red although im open to any colour/design scheme

VRK Ventures
Lewis Prentham
Managing Director
0419582147
lewis@vrkventures.com.au

```html
<!DOCTYPE html>
<html lang="en">
<head>
<meta charset="utf-8">
<title>VRK Ventures – Business Card</title>
<link href="https://fonts.googleapis.com/css2?family=Open+Sans:wght@300;400;600&display=swap" rel="stylesheet">
<style>
  :root {
    --bg: #e9e6e2;
    --paper: #ffffff;
    --brand-red: #c11a2e;
    --brand-red-light: #d23447;
    --ink-grey: #6b6b6d;
    --rule-grey: #b9b9bb;
    --on-red: #ffffff;
  }
  * { box-sizing: border-box; margin: 0; padding: 0; }
  html, body {
    width: 1200px; height: 1023px; overflow: hidden;
    background: var(--bg);
    font-family: "Open Sans", Arial, sans-serif;
  }
  .sheet {
    width: 1200px; height: 1023px;
    display: flex; flex-direction: column; align-items: center; justify-content: center;
    gap: 60px;
  }
  .card {
    position: relative;
    width: 700px; height: 400px;
    border-radius: 26px;
    overflow: hidden;
    background: var(--paper);
    box-shadow: 0 6px 18px rgba(0,0,0,0.18);
  }
  .card__band {
    position: absolute; left: 0; right: 0; bottom: 0;
    background: linear-gradient(100deg, var(--brand-red-light) 0%, var(--brand-red) 45%, var(--brand-red) 100%);
  }

  /* Front */
  .front .card__band { height: 150px; }
  .brand {
    position: absolute; left: 0; right: 0; top: 70px;
    display: flex; align-items: center; justify-content: center; gap: 16px;
  }
  .brand__dot {
    width: 22px; height: 22px; border-radius: 50%;
    background: var(--brand-red);
  }
  .brand__name {
    font-size: 50px; font-weight: 400; letter-spacing: 2px;
    color: var(--ink-grey); text-transform: uppercase;
  }
  .person {
    position: absolute; left: 40px; bottom: 38px; color: var(--on-red);
  }
  .person__name { font-size: 30px; font-weight: 600; letter-spacing: 0.5px; line-height: 1.2; }
  .person__title { font-size: 19px; font-weight: 300; letter-spacing: 0.5px; }
  .contact {
    position: absolute; right: 36px; bottom: 40px;
    color: var(--on-red); font-size: 17px; font-weight: 300; letter-spacing: 0.8px;
    display: flex; flex-direction: column; align-items: flex-end; gap: 12px;
  }
  .contact__row { display: flex; align-items: center; gap: 10px; }
  .contact__icon { width: 20px; height: 20px; }

  /* Back */
  .back .card__band { height: 180px; }
  .notes {
    position: absolute; left: 40px; right: 40px; top: 24px;
  }
  .notes__label {
    font-size: 14px; color: var(--ink-grey); letter-spacing: 1px; margin-bottom: 8px;
  }
  .notes__line {
    height: 1px; background: var(--rule-grey); margin-bottom: 26px;
  }
  .back .brand { top: auto; bottom: 62px; }
  .back .brand__dot { background: var(--on-red); }
  .back .brand__name { color: var(--on-red); font-size: 44px; }
</style>
</head>
<body>
<main class="sheet">
  <section class="card front" aria-label="Card front">
    <div class="brand">
      <span class="brand__dot"></span>
      <span class="brand__name">VRK Ventures</span>
    </div>
    <div class="card__band">
      <div class="person">
        <p class="person__name">Lewis Prentham</p>
        <p class="person__title">Managing Director</p>
      </div>
      <div class="contact">
        <p class="contact__row">0419582147
          <svg class="contact__icon" viewBox="0 0 20 20" aria-hidden="true">
            <circle cx="10" cy="10" r="9" fill="none" stroke="#fff" stroke-width="1.2"/>
            <path d="M7 5.5l2 2-1 1.2c.6 1.3 1.5 2.2 2.8 2.8l1.2-1 2 2-1.3 1.5C9.6 13.5 6.5 10.4 5.5 7.3z" fill="#fff"/>
          </svg>
        </p>
        <p class="contact__row">lewis@vrkventures.com.au
          <svg class="contact__icon" viewBox="0 0 20 20" aria-hidden="true">
            <circle cx="10" cy="10" r="9" fill="none" stroke="#fff" stroke-width="1.2"/>
            <rect x="5.5" y="7" width="9" height="6.5" fill="none" stroke="#fff" stroke-width="1.1"/>
            <path d="M5.5 7l4.5 3.6L14.5 7" fill="none" stroke="#fff" stroke-width="1.1"/>
          </svg>
        </p>
      </div>
    </div>
  </section>

  <section class="card back" aria-label="Card back">
    <div class="notes">
      <p class="notes__label">Notes</p>
      <div class="notes__line"></div>
      <div class="notes__line"></div>
      <div class="notes__line"></div>
      <div class="notes__line"></div>
      <div class="notes__line"></div>
      <div class="notes__line"></div>
    </div>
    <div class="card__band">
      <div class="brand">
        <span class="brand__dot"></span>
        <span class="brand__name">VRK Ventures</span>
      </div>
    </div>
  </section>
</main>
</body>
</html>
```